Visitenkarte für therapeutischen Dienstleister
Breits die ersten Designvorschläge deckten sich weitgehend mit meinem Briefing. Anfragen und Änderungen werden rasch und professionell beantwortet und umgesetzt.
Zielgruppe
siehe Briefing
Aufgabenstellung

```html
<!DOCTYPE html>
<html lang="fr">
<head>
<meta charset="utf-8">
<title>Atelier Corps – Carte de visite</title>
<link href="https://fonts.googleapis.com/css2?family=Inter:ital,wght@0,300;0,400;0,800;1,300&display=swap" rel="stylesheet">
<style>
  :root {
    --page: #e8e8e8;
    --card-white: #ffffff;
    --sand: #c2a584;
    --sand-light: #d9c3a8;
    --ink: #0a0a0a;
    --cream: #f6f1ea;
  }
  * { margin: 0; padding: 0; box-sizing: border-box; }
  html, body { width: 667px; height: 1200px; overflow: hidden; background: var(--page); }
  body { position: relative; font-family: "Inter", Arial, sans-serif; }

  .card {
    position: absolute; left: 53px; width: 564px; height: 357px;
    border-radius: 21px; overflow: hidden;
    box-shadow: 8px 10px 18px rgba(0,0,0,0.25);
  }
  .card--front { top: 213px; background: var(--card-white); }
  .card--back { top: 638px; background: var(--sand); }

  /* front */
  .brand { position: absolute; left: 30px; top: 46px; display: flex; align-items: center; gap: 10px; }
  .brand__mark { width: 22px; height: 22px; border-radius: 50%; background: var(--ink); }
  .brand__name { font-family: "Inter", Arial, sans-serif; font-weight: 400; font-size: 20px; color: var(--ink); letter-spacing: 0.01em; }

  .figure-front {
    position: absolute; right: 0; top: 18px; width: 160px; height: 330px;
    border-radius: 40px 0 0 60px;
    background: linear-gradient(160deg, var(--sand-light), var(--sand) 60%, #9a9a9a);
    opacity: .55;
  }

  .name { position: absolute; right: 165px; top: 172px; text-align: right; font-weight: 800; letter-spacing: -0.04em; line-height: 0.92; }
  .name__first { display: block; font-size: 68px; color: var(--sand); }
  .name__last { display: block; font-size: 68px; color: var(--ink); margin-top: 3px; }
  .title { position: absolute; right: 165px; top: 306px; font-size: 16px; font-style: italic; font-weight: 300; color: var(--ink); letter-spacing: -0.01em; }

  /* back */
  .figure-back {
    position: absolute; left: 0; top: 0; width: 166px; height: 357px;
    border-radius: 0 50px 60px 0;
    background: linear-gradient(170deg, var(--cream), #e9dfd2 55%, #b0a08d);
    opacity: .6;
  }
  .heading { position: absolute; right: 52px; top: 28px; text-align: right; color: var(--card-white); font-weight: 800; font-size: 27px; letter-spacing: -0.03em; line-height: 1.25; }

  .service { position: absolute; top: 106px; width: 130px; margin-left: -65px; text-align: center; }
  .service__label { font-size: 14px; font-weight: 400; color: var(--card-white); line-height: 1.3; }
  .service__icon { display: block; margin: 14px auto 0; width: 60px; height: 60px; border-radius: 8px; background: var(--ink); opacity: .85; }
  .service--massage { left: 210px; }
  .service--blocage { left: 343px; }
  .service--golf { left: 469px; }

  .divider { position: absolute; left: 168px; top: 236px; width: 344px; height: 2px; background: var(--cream); }

  .contact { position: absolute; right: 52px; top: 249px; text-align: right; color: var(--card-white); font-style: normal; font-weight: 300; font-size: 15.5px; line-height: 1.38; letter-spacing: -0.01em; }
  .contact__label { font-size: 14px; margin-bottom: 2px; }
</style>
</head>
<body>

<section class="card card--front">
  <div class="brand">
    <span class="brand__mark"></span>
    <span class="brand__name">Atelier Corps</span>
  </div>
  <div class="figure-front" role="img" aria-label="Illustration en silhouette d'une jambe tendue et d'une jambe au sol, tons sable"></div>
  <h1 class="name">
    <span class="name__first">MARC</span>
    <span class="name__last">LIRNWA</span>
  </h1>
  <p class="title">Masseur médical avec brevet fédéral</p>
</section>

<section class="card card--back">
  <div class="figure-back" role="img" aria-label="Illustration en silhouette de jambes, tons blancs et crème"></div>
  <h2 class="heading">THERAPIE MUSCULO<br>SQUELETTIQUE</h2>

  <div class="service service--massage">
    <p class="service__label">Atelier<br>massage</p>
    <span class="service__icon" role="img" aria-label="Pictogramme d'un massage sur une personne allongée"></span>
  </div>
  <div class="service service--blocage">
    <p class="service__label">Atelier blocage<br>sacro - ilaque</p>
    <span class="service__icon" role="img" aria-label="Pictogramme d'un bassin et de la colonne vertébrale"></span>
  </div>
  <div class="service service--golf">
    <p class="service__label">Atelier golf<br>thérapie</p>
    <span class="service__icon" role="img" aria-label="Pictogramme d'un golfeur tenant son club sur les épaules"></span>
  </div>

  <div class="divider"></div>

  <address class="contact">
    <p class="contact__label">Contact:</p>
    <p>Chemin des Tilleuls 14, 1205 Genève</p>
    <p>www.atelier-corps.ch</p>
    <p>079 000 12 34</p>
  </address>
</section>

</body>
</html>
```